Acupuncture business needs business card design

I need a business card for an acupuncture clinic called "Harbour Balance"
It will need the following details:
My name: Mark Tevita
Acupuncturist
Member KPTG
WFB Treatment Provider
Ph numbers: 512 8830 027 584 1176
Email: mark@hbneedle.example.nz
On the back it will need a table with 2 columns for appointments, one column for time and one for date.

Industry/Entity Type

Clinic

Contact Information for Business Card

Mark Tevita
Acupuncturist
Member KPTG
WFB Treatment Provider
Email: mark@hbneedle.example.nz

Requirements
Must have
• Mark Tevita
• Acupuncturist
• Member KPTG
• WFB Treatment Provider
• Ph numbers: 512 8830 027 584 1176
• Email: mark@hbneedle.example.nz
• On the back it will need a table with 2 columns for appointments, one column for time and one for date.

```html
<!DOCTYPE html>
<html lang="en">
<head>
<meta charset="utf-8">
<title>Harbour Balance – Business Card</title>
<link href="https://fonts.googleapis.com/css2?family=Open+Sans:wght@400;600;700&display=swap" rel="stylesheet">
<style>
  :root{
    --teal:#1aa3b5;
    --teal-dark:#0f8597;
    --teal-light:#3fc3d3;
    --sky:#2fb7e0;
    --paper:#ffffff;
    --paper-shade:#f4f6f7;
    --ink-soft:#7a8a8f;
    --backdrop:#e9e6e1;
  }
  *{box-sizing:border-box;margin:0;padding:0}
  html,body{width:1200px;height:1023px;overflow:hidden;background:var(--backdrop);font-family:"Open Sans",Arial,sans-serif}
  .card{position:absolute;width:620px;height:354px;background:var(--paper);border-radius:4px;box-shadow:0 12px 30px rgba(0,0,0,.18);overflow:hidden}
  .card svg.shape{position:absolute;inset:0;width:100%;height:100%}
  .card-front{left:50px;top:90px}
  .card-back{left:530px;top:570px}

  .brand{position:absolute;display:flex;align-items:center;gap:14px}
  .brand-dot{width:44px;height:44px;border-radius:50%;background:var(--teal);flex:none}
  .brand-name{font-weight:700;color:var(--teal);line-height:1;white-space:nowrap}
  .brand-tag{font-size:11px;letter-spacing:.42em;color:var(--ink-soft);margin-top:6px;text-transform:uppercase;white-space:nowrap}

  .card-front .brand{left:30px;top:36px}
  .card-front .brand-name{font-size:42px}

  .contact{position:absolute;left:336px;top:206px;color:#fff;font-size:13px;line-height:1.55}
  .contact .person{font-size:19px;font-weight:700;margin-bottom:4px;white-space:nowrap}
  .contact .person span{font-weight:400;font-size:15px;border-left:1px solid rgba(255,255,255,.8);padding-left:8px;margin-left:6px}
  .contact .row{display:flex;align-items:center;gap:8px;white-space:nowrap}
  .contact svg{width:12px;height:12px}

  .appointments{position:absolute;left:30px;top:26px;width:262px}
  .appointments h2{font-weight:400;font-size:26px;color:var(--teal-dark);margin-bottom:22px}
  .appt-table{width:100%;border-collapse:collapse;font-size:12px;color:var(--teal-dark)}
  .appt-table td{padding:14px 0 4px;white-space:nowrap}
  .appt-table .line{display:inline-block;width:72px;border-bottom:1px dotted var(--teal);margin-left:4px}

  .card-back .brand{right:24px;top:116px;flex-direction:column;align-items:flex-end;gap:10px;text-align:right}
  .card-back .brand-name{font-size:22px;color:#fff}
  .card-back .brand-tag{color:#e6f7fa;font-size:8px;letter-spacing:.3em}
  .card-back .brand-dot{width:32px;height:32px;background:#fff}
</style>
</head>
<body>

<section class="card card-front" aria-label="Business card front">
  <svg class="shape" viewBox="0 0 620 354" preserveAspectRatio="none">
    <defs>
      <linearGradient id="frontBand" x1="0" y1="0" x2="1" y2="1">
        <stop offset="0" stop-color="#3fc3d3"/>
        <stop offset="1" stop-color="#0f8597"/>
      </linearGradient>
    </defs>
    <path d="M120 354 C 170 230 300 150 620 90 L620 354 Z" fill="#2fb7e0"/>
    <path d="M140 354 C 190 240 318 162 620 104 L620 354 Z" fill="#ffffff"/>
    <path d="M150 354 C 200 246 326 168 620 110 L620 354 Z" fill="url(#frontBand)"/>
  </svg>
  <div class="brand">
    <div class="brand-dot"></div>
    <div>
      <div class="brand-name">Harbour Balance</div>
      <div class="brand-tag">Acupuncture Physiotherapy</div>
    </div>
  </div>
  <div class="contact">
    <div class="person">Mark Tevita<span>Acupuncturist</span></div>
    <div>Member KPTG</div>
    <div>WFB Treatment Provider</div>
    <div class="row">
      <svg viewBox="0 0 12 12"><rect x="3" y="1" width="6" height="10" rx="1" fill="none" stroke="#fff"/></svg>
      512 8830 027 584 1176
    </div>
    <div class="row">
      <svg viewBox="0 0 12 12"><rect x="1" y="2.5" width="10" height="7" fill="none" stroke="#fff"/><path d="M1 3l5 4 5-4" fill="none" stroke="#fff"/></svg>
      mark@hbneedle.example.nz
    </div>
  </div>
</section>

<section class="card card-back" aria-label="Business card back">
  <svg class="shape" viewBox="0 0 620 354" preserveAspectRatio="none">
    <defs>
      <linearGradient id="backBand" x1="0" y1="0" x2="1" y2="1">
        <stop offset="0" stop-color="#1aa3b5"/>
        <stop offset="1" stop-color="#0f8597"/>
      </linearGradient>
    </defs>
    <rect width="620" height="354" fill="#f4f6f7"/>
    <path d="M330 0 C 300 120 320 250 400 354 L620 354 L620 0 Z" fill="#2fb7e0"/>
    <path d="M344 0 C 314 120 334 250 416 354 L620 354 L620 0 Z" fill="#ffffff"/>
    <path d="M352 0 C 322 120 342 250 426 354 L620 354 L620 0 Z" fill="url(#backBand)"/>
  </svg>
  <div class="appointments">
    <h2>Appointments</h2>
    <table class="appt-table">
      <tr><td>Time:<span class="line"></span></td><td>Date:<span class="line"></span></td></tr>
      <tr><td>Time:<span class="line"></span></td><td>Date:<span class="line"></span></td></tr>
      <tr><td>Time:<span class="line"></span></td><td>Date:<span class="line"></span></td></tr>
      <tr><td>Time:<span class="line"></span></td><td>Date:<span class="line"></span></td></tr>
    </table>
  </div>
  <div class="brand">
    <div class="brand-dot"></div>
    <div>
      <div class="brand-name">Harbour Balance</div>
      <div class="brand-tag">Acupuncture Physiotherapy</div>
    </div>
  </div>
</section>

</body>
</html>
```